CD-/Plattencover
Zielgruppe
Labelname: 'Kiesel & Fackel Label'; Produktion von Popmusik
Aufgabenstellung
Die Texte der Songs gehen massiv in die Tiefe und werden freundlich und sanft vorgebracht. Die Musik hat einen leichten Countryblues-Touch.
Ich brauche auf der Rückseite der EP sämtliche Spezifikationen, die auf einer CD verlangt werden.
Der Titel lautet 'Morgenrot, Tauwind' und bezieht sich auf die Kürze des Lebens. Die Grundstimmung der Musik ist dennoch fröhlich (ironisch).

```html
<!DOCTYPE html>
<html lang="de">
<head>
<meta charset="utf-8">
<title>Morgenrot, Tauwind – Cover und Disc</title>
<link rel="stylesheet" href="https://fonts.googleapis.com/css2?family=Cormorant+Garamond:wght@300;400&family=Mrs+Saint+Delafield&display=swap">
<style>
  :root {
    --stage: #2a7a5e;
    --sky-top: #cdbfc4;
    --sky-light: #efe3cf;
    --glow: #e9b35a;
    --mountain: #3f4a36;
    --field: #8a6a2a;
    --field-dark: #3d3318;
    --tan: #b69b86;
    --ink: #2b1a12;
    --white: #fbf7f1;
    --hub: #9aa3a0;
  }
  * { margin: 0; padding: 0; box-sizing: border-box; }
  html, body { width: 1200px; height: 789px; overflow: hidden; }
  body { background: var(--stage); position: relative; font-family: "Cormorant Garamond", serif; }

  .cover {
    position: absolute; left: 60px; top: 95px; width: 600px; height: 600px;
    overflow: hidden; box-shadow: 0 14px 40px rgba(0,0,0,.35);
  }
  .cover__photo {
    position: absolute; inset: 0;
    background:
      radial-gradient(ellipse 45% 35% at 48% 62%, rgba(255,214,130,.95), rgba(233,179,90,.0) 70%),
      linear-gradient(105deg, rgba(0,0,0,0) 60%, var(--mountain) 78%, #2e3526 100%),
      linear-gradient(180deg, var(--sky-top) 0%, var(--sky-light) 35%, var(--glow) 60%, var(--field) 66%, var(--field-dark) 100%);
  }
  .cover__title {
    position: absolute; left: 160px; top: 300px; color: var(--white); white-space: nowrap;
  }
  .title__script {
    display: block; font-family: "Mrs Saint Delafield", cursive;
    font-size: 60px; line-height: 1; color: var(--ink); margin-left: 16px;
  }
  .title__main {
    display: block; font-family: "Cormorant Garamond", serif; font-weight: 300;
    font-size: 76px; letter-spacing: 2px; line-height: .9; margin-top: -4px;
  }

  .disc { position: absolute; left: 710px; top: 175px; width: 440px; height: 440px; filter: drop-shadow(0 12px 24px rgba(0,0,0,.35)); }
  .disc__script { font-family: "Mrs Saint Delafield", cursive; font-size: 34px; fill: var(--ink); }
  .disc__title { font-family: "Cormorant Garamond", serif; font-weight: 300; font-size: 32px; fill: var(--white); letter-spacing: 1px; }
  .disc__label { font-family: "Cormorant Garamond", serif; font-size: 15px; fill: var(--ink); }
  .disc__address { font-family: "Cormorant Garamond", serif; font-size: 9px; fill: var(--ink); }
</style>
</head>
<body>
  <section class="cover">
    <div class="cover__photo" role="img" aria-label="Foto: Berglandschaft bei Sonnenaufgang, Wolkenhimmel, felsiger Berg rechts, goldenes Grasfeld"></div>
    <h1 class="cover__title">
      <span class="title__script">Morgenrot</span>
      <span class="title__main">TAUWIND</span>
    </h1>
  </section>

  <svg class="disc" viewBox="0 0 440 440" aria-label="CD-Label">
    <defs>
      <clipPath id="disc-shape"><circle cx="220" cy="220" r="218"/></clipPath>
      <linearGradient id="disc-photo" x1="0" y1="0" x2="0" y2="1">
        <stop offset="0" stop-color="#cfc3c4"/>
        <stop offset=".35" stop-color="#7f8a80"/>
        <stop offset=".55" stop-color="#38452f"/>
        <stop offset=".65" stop-color="#7a5e28"/>
        <stop offset="1" stop-color="#3d3318"/>
      </linearGradient>
    </defs>
    <g clip-path="url(#disc-shape)">
      <rect class="disc__photo" width="440" height="440" fill="url(#disc-photo)" role="img" aria-label="Foto: Berg und Grasfeld, Ausschnitt des Covermotivs"/>
      <polygon points="0,0 200,0 420,440 0,440" fill="var(--tan)"/>
    </g>
    <circle cx="220" cy="220" r="217" fill="none" stroke="rgba(255,255,255,.35)" stroke-width="2"/>
    <circle cx="220" cy="220" r="72" fill="var(--hub)"/>
    <circle cx="220" cy="220" r="48" fill="var(--stage)"/>
    <text class="disc__script" x="58" y="106">Morgenrot</text>
    <text class="disc__title" x="48" y="138">TAUWIND</text>
    <rect x="190" y="343" width="11" height="11" fill="var(--ink)"/>
    <text class="disc__label" x="208" y="354">kiesel &amp; fackel LABEL</text>
    <text class="disc__address" x="330" y="374" text-anchor="end">kiesel &amp; fackel LABEL</text>
    <text class="disc__address" x="330" y="385" text-anchor="end">Lutz W. Brenneke</text>
    <text class="disc__address" x="330" y="396" text-anchor="end">Am Kirchsteig 14C</text>
    <text class="disc__address" x="330" y="407" text-anchor="end">3421 Lindhof · Österreich</text>
  </svg>
</body>
</html>
```